Business Consulting Company needs a business card designed

We need a business card in Brisbane Australia for a company called " Brindlewood Consulting Group". I would like to see the designs either in purple or green color

```html
<!DOCTYPE html>
<html lang="en">
<head>
<meta charset="utf-8">
<title>Brindlewood Consulting Group – Business Card</title>
<link rel="stylesheet" href="https://fonts.googleapis.com/css2?family=Cinzel:wght@500&family=Open+Sans:wght@300;400&display=swap">
<style>
  :root {
    --bg: #eceef0;
    --card: #ffffff;
    --green-deep: #1c7447;
    --green-light: #4cc088;
    --brand: #23864f;
    --ink-light: #ffffff;
    --edge: #c9ccd0;
  }
  * { margin: 0; padding: 0; box-sizing: border-box; }
  html, body { width: 1200px; height: 900px; overflow: hidden; }
  body {
    background: var(--bg);
    display: flex;
    flex-direction: column;
    align-items: center;
    justify-content: center;
    gap: 60px;
    font-family: "Open Sans", sans-serif;
  }
  .card {
    position: relative;
    width: 660px;
    height: 380px;
    border-radius: 30px;
    background: var(--card);
    overflow: hidden;
    box-shadow: 0 2px 0 var(--edge), 0 10px 24px rgba(0,0,0,0.12);
  }
  .card-shape { position: absolute; inset: 0; }
  .contact-block {
    position: absolute;
    left: 36px;
    top: 34px;
    color: var(--ink-light);
  }
  .person-name {
    font-size: 17px;
    font-weight: 400;
    letter-spacing: 0.5px;
    text-transform: uppercase;
  }
  .person-title { font-size: 13px; font-weight: 300; margin-top: 2px; }
  .address { font-size: 12.5px; font-weight: 300; margin-top: 28px; line-height: 1.45; }
  .contact-list { list-style: none; margin-top: 20px; font-size: 12.5px; font-weight: 300; }
  .contact-list li { display: flex; align-items: center; gap: 9px; height: 20px; }
  .contact-list svg { width: 12px; height: 12px; fill: var(--ink-light); flex: none; }
  .brand {
    position: absolute;
    display: flex;
    flex-direction: column;
    align-items: center;
    color: var(--brand);
    font-family: "Cinzel", serif;
    font-weight: 500;
    text-align: center;
    line-height: 1.15;
    white-space: nowrap;
  }
  .brand-dot {
    width: 40px; height: 40px;
    border-radius: 50%;
    background: var(--brand);
    margin-bottom: 10px;
  }
  .card-front .brand { left: 300px; right: 20px; top: 130px; font-size: 20px; }
  .card-back .brand { left: 0; right: 0; top: 120px; font-size: 27px; }
  .card-back .brand-dot { width: 50px; height: 50px; margin-bottom: 14px; }
</style>
</head>
<body>

  <section class="card card-front">
    <svg class="card-shape" viewBox="0 0 660 380" aria-hidden="true">
      <defs>
        <linearGradient id="panelFill" x1="0" y1="1" x2="1" y2="0">
          <stop offset="0" stop-color="#1c7447"/>
          <stop offset="1" stop-color="#4cc088"/>
        </linearGradient>
        <linearGradient id="swoosh" x1="0" y1="0" x2="0" y2="1">
          <stop offset="0" stop-color="#ffffff"/>
          <stop offset="0.5" stop-color="#8d9297"/>
          <stop offset="1" stop-color="#dfe2e5"/>
        </linearGradient>
      </defs>
      <path d="M0 0 H300 C262 90 252 260 236 380 H0 Z" fill="url(#panelFill)"/>
      <path d="M304 0 C266 90 256 260 240 380" fill="none" stroke="url(#swoosh)" stroke-width="7"/>
    </svg>

    <div class="contact-block">
      <p class="person-name">Liam Prescott</p>
      <p class="person-title">Managing Director</p>
      <p class="address">Level 12, 140 Ann Street<br>Brisbane QLD 4000</p>
      <ul class="contact-list">
        <li><svg viewBox="0 0 12 12"><path d="M2.5 1 L4.5 1 L5.3 3.5 L4 4.5 C4.7 6 6 7.3 7.5 8 L8.5 6.7 L11 7.5 L11 9.5 C11 10.3 10.3 11 9.5 11 C5 10.8 1.2 7 1 2.5 C1 1.7 1.7 1 2.5 1 Z"/></svg>07 3100 4820</li>
        <li><svg viewBox="0 0 12 12"><path d="M3 1 H9 V11 H3 Z M4 2 V9 H8 V2 Z"/></svg>0412 558 903</li>
        <li><svg viewBox="0 0 12 12"><path d="M1 3 H11 V10 H1 Z M1.8 3.6 L6 6.8 L10.2 3.6 V9.3 H1.8 Z" fill-rule="evenodd"/></svg>hello@brindlewoodcg.com</li>
        <li><svg viewBox="0 0 12 12"><path d="M6 1 A5 5 0 1 0 6 11 A5 5 0 1 0 6 1 Z M6 2 A4 4 0 1 1 6 10 A4 4 0 1 1 6 2 Z M1.5 5.5 H10.5 V6.5 H1.5 Z M5.5 1.5 H6.5 V10.5 H5.5 Z" fill-rule="evenodd"/></svg>www.brindlewoodcg.com.au</li>
      </ul>
    </div>

    <div class="brand">
      <span class="brand-dot" aria-hidden="true"></span>
      <span>Brindlewood Consulting</span>
      <span>Group</span>
    </div>
  </section>

  <section class="card card-back">
    <div class="brand">
      <span class="brand-dot" aria-hidden="true"></span>
      <span>Brindlewood Consulting</span>
      <span>Group</span>
    </div>
  </section>

</body>
</html>
```